logo for security & safety training, education consultants
Marlow Advisory Nest Pte Ltd
Professional
LTC (RET) LIM BOON KEAT ROBERT MBA
DIRECTOR
47 JALAN TEMBUSIRA SINGAPORE 528806
robert@marlownest-example.com
www.marlownest-example.com
Perhaps some iso logo and same award logo in dummies

```html
<!DOCTYPE html>
<html lang="en">
<head>
<meta charset="utf-8">
<title>Marlow Advisory Nest — Business Card</title>
<link rel="stylesheet" href="https://fonts.googleapis.com/css2?family=Open+Sans:wght@400;600;800&display=swap">
<style>
  :root {
    --page-bg: #e9e9e9;
    --card-bg: #ffffff;
    --brand-blue: #2b3a9e;
    --ink: #1b1b1b;
    --muted: #555555;
    --rule: #b9b9b9;
  }
  * { box-sizing: border-box; margin: 0; padding: 0; }
  html, body { width: 1200px; height: 991px; overflow: hidden; }
  body {
    background: var(--page-bg);
    font-family: "Open Sans", Arial, sans-serif;
    color: var(--ink);
    display: flex;
    flex-direction: column;
    align-items: center;
    justify-content: center;
    gap: 60px;
  }
  .card {
    width: 640px;
    height: 373px;
    background: var(--card-bg);
    box-shadow: 0 6px 18px rgba(0,0,0,0.14);
    position: relative;
    overflow: hidden;
  }
  .brand {
    display: flex;
    flex-direction: column;
    align-items: center;
    gap: 10px;
  }
  .brand-dot {
    width: 16px; height: 16px;
    border-radius: 50%;
    background: var(--brand-blue);
  }
  .brand-name {
    font-weight: 800;
    color: var(--brand-blue);
    letter-spacing: 1px;
    line-height: 1;
    white-space: nowrap;
  }
  .card-front { display: flex; align-items: center; justify-content: center; }
  .card-front .brand-name { font-size: 48px; }

  .card-back { display: flex; align-items: center; padding-left: 30px; }
  .card-back .brand { width: 240px; padding-right: 20px; }
  .card-back .brand-name { font-size: 44px; }
  .divider {
    flex: none;
    width: 1px; height: 190px;
    background: var(--rule);
  }
  .contact { padding-left: 22px; width: 340px; }
  .person-name {
    font-size: 12px; font-weight: 600;
    color: var(--brand-blue);
    line-height: 1.3;
    white-space: nowrap;
  }
  .person-role {
    font-size: 9px; color: var(--muted);
    letter-spacing: 1px; margin-bottom: 26px;
  }
  .contact-list { list-style: none; display: flex; flex-direction: column; gap: 5px; }
  .contact-item {
    display: flex; align-items: flex-start; gap: 8px;
    font-size: 11px; color: var(--muted); line-height: 1.35;
  }
  .contact-icon {
    flex: none; width: 13px; height: 13px;
    border-radius: 50%; background: var(--brand-blue);
    display: flex; align-items: center; justify-content: center;
    margin-top: 1px;
  }
  .contact-icon svg { width: 8px; height: 8px; fill: #fff; }
</style>
</head>
<body>
  <section class="card card-front" aria-label="Card front">
    <div class="brand">
      <span class="brand-dot"></span>
      <span class="brand-name">MARLOW</span>
    </div>
  </section>

  <section class="card card-back" aria-label="Card back">
    <div class="brand">
      <span class="brand-dot"></span>
      <span class="brand-name">MARLOW</span>
    </div>
    <div class="divider"></div>
    <div class="contact">
      <p class="person-name">LTC (RET) LIM BOON KEAT ROBERT MBA</p>
      <p class="person-role">DIRECTOR</p>
      <ul class="contact-list">
        <li class="contact-item">
          <span class="contact-icon"><svg viewBox="0 0 10 10"><path d="M5 0a3.5 3.5 0 0 0-3.5 3.5C1.5 6 5 10 5 10s3.5-4 3.5-6.5A3.5 3.5 0 0 0 5 0zm0 5a1.5 1.5 0 1 1 0-3 1.5 1.5 0 0 1 0 3z"/></svg></span>
          <span>47 JALAN TEMBUSIRA<br>SINGAPORE 528806</span>
        </li>
        <li class="contact-item">
          <span class="contact-icon"><svg viewBox="0 0 10 10"><path d="M2 0l2 2.5-1 1.2a6 6 0 0 0 3.3 3.3l1.2-1L10 8l-1.5 2C4 10 0 6 0 1.5z"/></svg></span>
          <span>+65 60140231</span>
        </li>
        <li class="contact-item">
          <span class="contact-icon"><svg viewBox="0 0 10 10"><rect x="2.5" y="0" width="5" height="10" rx="1"/></svg></span>
          <span>+65 90457213</span>
        </li>
        <li class="contact-item">
          <span class="contact-icon"><svg viewBox="0 0 10 10"><rect x="1" y="3" width="8" height="5"/><rect x="2.5" y="1" width="5" height="2"/></svg></span>
          <span>+65 6318 2047</span>
        </li>
        <li class="contact-item">
          <span class="contact-icon"><svg viewBox="0 0 10 10"><path d="M0 2h10v6H0z M0 2l5 3.5L10 2" stroke="#2b3a9e" stroke-width="0.8"/></svg></span>
          <span>robert@marlownest-example.com</span>
        </li>
        <li class="contact-item">
          <span class="contact-icon"><svg viewBox="0 0 10 10"><circle cx="5" cy="5" r="4" fill="none" stroke="#fff" stroke-width="1"/><path d="M1 5h8M5 1v8" stroke="#fff" stroke-width="0.8"/></svg></span>
          <span>www.marlownest-example.com</span>
        </li>
      </ul>
    </div>
  </section>
</body>
</html>
```